Redesign of Business Card to look more professional and stand out

Business card design. You can lean more about our company by going to dkrfabworks.example. Raised letters would be nice. Company name & Address
DK&R
418 Wendlow Ridge Drive, Suite 340
Fernbrook, AL 36019

You can use my name and title: Glenn Harwick
Business Development Manager

Target Market(s)

Heavy Industrial market, i.e. utilities, chemical plants, paper mills, construction companies

Industry/Entity Type

Construction

Contact Information for Business Card

We provide Project Management & Project Support Services

Font styles to use
Serif

Requirements
Must have
• Company name & Address
• DK&R
• 418 Wendlow Ridge Drive, Suite 340
• Fernbrook, AL 36019
Nice to have
• ideas for the back of the card
Should not have
• no crazy colors. needs to look professional and standout.

```html
<!DOCTYPE html>
<html lang="en">
<head>
<meta charset="utf-8">
<title>DK&amp;R Business Card</title>
<link rel="stylesheet" href="https://fonts.googleapis.com/css2?family=Noto+Serif:wght@400;700&display=swap">
<style>
  :root {
    --backdrop: #74cfbe;
    --navy: #1e3566;
    --steel-blue: #2a4d8c;
    --paper: #ffffff;
    --ink-address: #2c3565;
    --ink-light: #ece6f4;
    --serif: "Noto Serif", Georgia, serif;
  }
  html, body {
    margin: 0;
    padding: 0;
    width: 1200px;
    height: 750px;
    overflow: hidden;
    background: var(--backdrop);
  }
  .canvas {
    position: relative;
    width: 1200px;
    height: 750px;
  }
  .card {
    position: absolute;
    top: 249px;
    width: 420px;
    height: 252px;
    overflow: hidden;
  }
  .card--front { left: 150px; background: var(--navy); }
  .card--back  { left: 630px; background: var(--paper); }

  /* Front side: framed company name */
  .front-frame {
    position: absolute;
    left: 60px;
    top: 69px;
    width: 300px;
    height: 114px;
    box-sizing: border-box;
    background: var(--paper);
    padding: 8px;
  }
  .front-frame__inner {
    width: 100%;
    height: 100%;
    box-sizing: border-box;
    border: 3px solid var(--navy);
    display: flex;
    align-items: center;
    justify-content: center;
  }
  .company-name {
    font-family: var(--serif);
    font-weight: 700;
    color: var(--navy);
    margin: 0;
    line-height: 1;
  }
  .front-frame .company-name { font-size: 50px; }

  /* Back side: angled panels and details */
  .back-panels {
    position: absolute;
    inset: 0;
    width: 420px;
    height: 252px;
  }
  .back-panels .panel--navy { fill: var(--navy); }
  .back-panels .panel--steel { fill: var(--steel-blue); }

  .back-brand {
    position: absolute;
    left: 22px;
    top: 18px;
    font-size: 40px;
  }
  .address {
    position: absolute;
    left: 12px;
    top: 68px;
    margin: 0;
    font-family: var(--serif);
    font-style: normal;
    font-size: 12px;
    line-height: 15px;
    color: var(--ink-address);
  }
  .address span { display: block; }
  .address .address__city { margin-left: -1px; }

  .person {
    position: absolute;
    right: 6px;
    bottom: 11px;
    text-align: right;
    font-family: var(--serif);
    color: var(--ink-light);
  }
  .person__name {
    margin: 0;
    font-size: 18px;
    font-weight: 400;
    line-height: 25px;
  }
  .person__title {
    margin: 0;
    font-size: 20px;
    line-height: 25px;
  }
</style>
</head>
<body>
<main class="canvas">
  <section class="card card--front" aria-label="Card front">
    <div class="front-frame">
      <div class="front-frame__inner">
        <p class="company-name">DK&amp;R</p>
      </div>
    </div>
  </section>

  <section class="card card--back" aria-label="Card back">
    <svg class="back-panels" viewBox="0 0 420 252" aria-hidden="true">
      <polygon class="panel--navy" points="0,252 131,195 420,65 420,252"/>
      <polygon class="panel--steel" points="0,252 0,99 131,195"/>
    </svg>
    <p class="company-name back-brand">DK&amp;R</p>
    <address class="address">
      <span>418 Wendlow Ridge Drive, Suite 340</span>
      <span class="address__city">Fernbrook, AL 36019</span>
    </address>
    <div class="person">
      <p class="person__name">Glenn Harwick</p>
      <p class="person__title">Business Development Manager</p>
    </div>
  </section>
</main>
</body>
</html>
```